Graphic Design Project

ok I have the artwork for my presentation folder, and I have the text to put on the folder, I need you to apply text to the folder and the single sheets, so inside the artwork is pictures to use, text to use. thank you so much ask me as many questions as you need
Updates

my girl forgot to upload the mock ups of the presentation folder and single sheets, my apologies please check updated files

Hey Guys this is a eazy project the artwork is done, the text is done, the pictures are done!, all you have to do is assemble the project, I even have mock up pictures of how project looks finished, I have made the money good so that you would not pass on this project because it is not that creative of a job!

Target Market(s)

Dr's and patients

Industry/Entity Type

Graphic Design

Requirements
Must have
• use the single sheet artwork to make as many single sheets as you need to use all of the text supplied
Should not have
• do not make this, so professional looking that it does not appeal to the patients

```html
<!DOCTYPE html>
<html lang="en">
<head>
<meta charset="utf-8">
<title>KindPath Counseling – Information Sheet</title>
<link href="https://fonts.googleapis.com/css2?family=Arimo:wght@400;700&display=swap" rel="stylesheet">
<style>
  :root {
    --backdrop-grey: #cdcdcd;
    --backdrop-sand: #d8cfbf;
    --backdrop-cream: #ebe6dc;
    --band-white: #ffffff;
    --panel: #f1f1f1;
    --ink: #2b2b2b;
    --ink-strong: #111111;
    --title-grey: #333333;
    --photo-frame: #ffffff;
    --photo-warm: #c9a55a;
    --photo-dark: #3a3f4a;
  }
  * { margin: 0; padding: 0; box-sizing: border-box; }
  html, body { width: 927px; height: 1200px; overflow: hidden; }
  body { font-family: "Arimo", Arial, sans-serif; background: var(--backdrop-grey); }
  .sheet { position: relative; width: 927px; height: 1200px; overflow: hidden; }
  .backdrop { position: absolute; inset: 0; }
  .content-panel {
    position: absolute; left: 50px; top: 48px; width: 839px; height: 1096px;
    background: var(--panel); border-radius: 16px;
  }
  .sheet-title {
    position: absolute; left: 0; right: 0; top: 30px; text-align: center;
    font-size: 30px; font-weight: 700; color: var(--title-grey);
  }
  .body-copy {
    position: absolute; left: 51px; width: 738px; top: 85px;
    font-size: 17.5px; line-height: 23.6px; color: var(--ink); text-align: justify;
  }
  .body-copy p { margin-bottom: 22px; }
  .brand-name { font-weight: 700; color: var(--ink-strong); }
  .photo-frame {
    position: absolute; left: 95px; top: 646px; width: 643px; height: 427px;
    background: var(--photo-frame); padding: 9px;
  }
  .photo-area {
    width: 100%; height: 100%;
    background:
      radial-gradient(ellipse at 55% 55%, #e8d8c0 0%, rgba(232,216,192,0) 35%),
      linear-gradient(90deg, var(--photo-dark) 0%, #5b6470 25%, var(--photo-warm) 45%, #d9b977 60%, #6b5a4a 80%, #4d3f35 100%);
  }
</style>
</head>
<body>
<div class="sheet">
  <svg class="backdrop" width="927" height="1200" viewBox="0 0 927 1200" aria-hidden="true">
    <rect width="927" height="1200" fill="var(--backdrop-grey)"/>
    <polygon points="650,0 927,0 927,60" fill="var(--band-white)"/>
    <polygon points="0,690 200,712 927,820 927,1200 0,1200" fill="var(--backdrop-sand)"/>
    <polygon points="850,600 927,580 927,1200 830,1200" fill="var(--backdrop-cream)"/>
    <path d="M0,680 L260,712 L0,760 Z" fill="var(--band-white)"/>
    <path d="M820,1200 C860,1120 900,1080 927,1040 L927,1070 C905,1100 875,1140 850,1200 Z" fill="var(--band-white)"/>
    <path d="M860,900 L927,860 L927,880 L870,915 Z" fill="var(--band-white)"/>
  </svg>

  <main class="content-panel">
    <h1 class="sheet-title">KindPath Counseling</h1>
    <div class="body-copy">
      <p><span class="brand-name">KindPath Counseling</span> will provide education, assessments, prevention and screening for those individuals with chronic pain and substance use disorders.</p>
      <p><span class="brand-name">KindPath Counseling</span> is a proactive addiction counseling center dedicated to addressing health issues in an integrated manner by working with pain management physicians to offer opioid education to prevent substance use and misuse disorders to their patients.</p>
      <p>Many pain management clinics and primary care physicians are interested in reducing risk to their patients and practice from opioid misuse and increasing quality care for their patients. Physicians are excited to have a service like <span class="brand-name">KindPath Counseling</span> to provide education and screening services for their patients.</p>
      <p><span class="brand-name">KindPath Counseling</span> services are provided by highly trained and caring professionals who are experienced in working in all areas of patient education, prevention and care.</p>
      <p><span class="brand-name">KindPath Counseling</span> is a resource for pain management clinics and primary care physicians to educate, assess and provide prevention and counseling to patients to reduce the risk of substance use disorders.</p>
    </div>
    <figure class="photo-frame">
      <div class="photo-area" role="img" aria-label="Photo of two people holding hands in support, against a soft autumn-leaf background"></div>
    </figure>
  </main>
</div>
</body>
</html>
```